Keystone Sales Group looking for inspirational poster

I need an inspirational poster design for sales professionals, targeted around the phrase "Win Fast, Lose Fast". The style of the poster will be primarily minimalistic and flat with the main focus being on the phrase, however, any graphics or creative font and background styles are encouraged. Color choice is up to you.

Design Specs:
Vector files are best. If creating a vector file isn't possible, 150dpi raster images (at actual size or bigger) are good too. The poster must be in a portrait layout and scalable to the sizes of 18" X 24" and 24" X 36". Please convert all text to outlines.

Please msg me if you have any additional questions.

```html
<!DOCTYPE html>
<html lang="en">
<head>
<meta charset="utf-8">
<title>Win Fast Lose Fast — Poster</title>
<link rel="stylesheet" href="https://fonts.googleapis.com/css2?family=Archivo+Black&family=Open+Sans:wght@400&display=swap">
<style>
  :root {
    --backdrop: #cfe5e4;
    --poster-white: #ffffff;
    --poster-blue: #1567c8;
  }
  html, body {
    margin: 0;
    padding: 0;
    width: 1200px;
    height: 1000px;
    overflow: hidden;
    background: var(--backdrop);
  }
  .canvas {
    display: block;
    width: 1200px;
    height: 1000px;
  }
  .headline {
    font-family: "Archivo Black", "Arial Black", sans-serif;
  }
  .headline--blue { fill: var(--poster-blue); }
  .headline--white { fill: var(--poster-white); }
  .brand-name {
    font-family: "Open Sans", Arial, sans-serif;
    font-size: 12px;
    fill: var(--poster-white);
  }
  .brand-rule {
    stroke: var(--poster-white);
    stroke-width: 1;
  }
</style>
</head>
<body>
<svg class="canvas" viewBox="0 0 1200 1000" xmlns="http://www.w3.org/2000/svg" aria-labelledby="poster-title">
  <title id="poster-title">Win Fast, Lose Fast</title>

  <g class="poster">
    <!-- sheet halves -->
    <rect class="sheet-top" x="245" y="27" width="711" height="473" fill="var(--poster-white)"/>
    <rect class="sheet-bottom" x="245" y="500" width="711" height="473" fill="var(--poster-blue)"/>

    <!-- square frame, colours inverted against each half -->
    <g class="frame-top" fill="var(--poster-blue)">
      <rect x="324" y="225" width="553" height="20"/>
      <rect x="324" y="225" width="20" height="275"/>
      <rect x="857" y="225" width="20" height="275"/>
    </g>
    <g class="frame-bottom" fill="var(--poster-white)">
      <rect x="324" y="758" width="553" height="20"/>
      <rect x="324" y="500" width="20" height="278"/>
      <rect x="857" y="500" width="20" height="278"/>
    </g>

    <!-- headline -->
    <g class="headline">
      <text class="headline--blue" x="549" y="412" font-size="40" textLength="70" lengthAdjust="spacingAndGlyphs">Win</text>
      <text class="headline--blue" x="549" y="500" font-size="118" textLength="247" lengthAdjust="spacingAndGlyphs">Fast</text>
      <text class="headline--white" x="549" y="522" font-size="26" textLength="70" lengthAdjust="spacingAndGlyphs">Lose</text>
      <text class="headline--white" x="549" y="612" font-size="118" textLength="247" lengthAdjust="spacingAndGlyphs">Fast</text>
    </g>

    <!-- brand line -->
    <g class="brand">
      <text class="brand-name" x="600" y="915" text-anchor="middle" textLength="153" lengthAdjust="spacing">Keystone Sales Group</text>
      <line class="brand-rule" x1="524" y1="918.5" x2="677" y2="918.5"/>
    </g>
  </g>
</svg>
</body>
</html>
```